Healthcare IT company looking for business card design

We develop IT systems for healthcare that significantly reduces cost and improves quality.

We want a business card design that is professional and clean, and using the colors in our logo.

Target Market(s)

Doctors and decision makers in the healthcare industry

Industry/Entity Type

Healthcare

Contact Information for Business Card

It should include
Name and title, address, telephone

Tobias Vrenholt, CEO
+46 712 418257
tobias@kelvaro.se

Font styles to use
Serif

Colors
0355a3
ed282f

Requirements
Must have
• Clean design
• Professional feel
Nice to have
• N/A
Should not have
• N/A

```html
<!DOCTYPE html>
<html lang="en">
<head>
<meta charset="utf-8">
<title>Kelvaro Business Card</title>
<link rel="stylesheet" href="https://fonts.googleapis.com/css2?family=Nunito:wght@800&family=Open+Sans:wght@400;600&family=Tinos:wght@700&display=swap">
<style>
  :root {
    --brand-blue: #0355a3;
    --brand-red: #ed282f;
    --paper: #ffffff;
    --stage: #2b2b2d;
    --ink-light: #ffffff;
  }
  * { margin: 0; padding: 0; box-sizing: border-box; }
  html, body { width: 1200px; height: 900px; overflow: hidden; background: var(--stage); }
  .canvas { position: relative; width: 1200px; height: 900px; }
  .card {
    position: absolute;
    width: 640px;
    height: 365px;
    border-radius: 22px;
    overflow: hidden;
  }
  .card-front {
    left: 150px; top: 60px;
    background: var(--brand-red);
    display: flex; align-items: center; justify-content: center; gap: 22px;
  }
  .front-dot {
    width: 54px; height: 54px; border-radius: 50%;
    background: var(--paper);
  }
  .front-name {
    font-family: "Nunito", sans-serif;
    font-weight: 800;
    font-size: 92px;
    color: var(--paper);
    letter-spacing: -1px;
  }
  .card-back {
    left: 410px; top: 475px;
    background: var(--paper);
  }
  .back-shape { position: absolute; inset: 0; }
  .brand {
    position: absolute; left: 36px; top: 110px;
    display: flex; align-items: center; gap: 14px;
  }
  .brand-dot {
    width: 30px; height: 30px; border-radius: 50%;
    background: var(--brand-red);
  }
  .brand-name {
    font-family: "Nunito", sans-serif;
    font-weight: 800;
    font-size: 86px;
    color: var(--brand-blue);
    letter-spacing: -1px;
  }
  .contact {
    position: absolute; right: 28px; top: 118px;
    text-align: right;
    color: var(--ink-light);
    font-family: "Open Sans", sans-serif;
  }
  .contact-name {
    font-family: "Tinos", serif;
    font-weight: 700;
    font-size: 19px;
    text-transform: uppercase;
    letter-spacing: 0.5px;
  }
  .contact-title { font-size: 12px; margin-bottom: 16px; }
  .contact-address { font-size: 13px; line-height: 1.4; margin-bottom: 6px; padding-right: 24px; }
  .contact-line {
    font-size: 13px; line-height: 1.6;
    display: flex; justify-content: flex-end; align-items: center; gap: 8px;
  }
  .contact-line svg { width: 14px; height: 14px; }
  .contact-line.no-icon { padding-right: 22px; }
</style>
</head>
<body>
<main class="canvas">
  <section class="card card-front" aria-label="Card front">
    <span class="front-dot"></span>
    <span class="front-name">Kelvaro</span>
  </section>

  <section class="card card-back" aria-label="Card back">
    <svg class="back-shape" viewBox="0 0 640 365" preserveAspectRatio="none" aria-hidden="true">
      <path d="M560 0 C420 40 335 180 325 365 L640 365 L640 0 Z" fill="var(--brand-red)"/>
      <path d="M640 24 C470 55 352 190 342 365 L640 365 Z" fill="var(--brand-blue)"/>
    </svg>

    <div class="brand">
      <span class="brand-name">Kelvaro</span>
      <span class="brand-dot"></span>
    </div>

    <div class="contact">
      <p class="contact-name">Tobias Vrenholt</p>
      <p class="contact-title">CEO</p>
      <p class="contact-address">Harbor Lane, 21480<br>Halden, Norway</p>
      <p class="contact-line">+46 712 418257
        <svg viewBox="0 0 24 24" aria-hidden="true"><path fill="#fff" d="M6.6 10.8a15.1 15.1 0 0 0 6.6 6.6l2.2-2.2a1 1 0 0 1 1-.25 11.4 11.4 0 0 0 3.6.57 1 1 0 0 1 1 1V20a1 1 0 0 1-1 1A17 17 0 0 1 3 4a1 1 0 0 1 1-1h3.5a1 1 0 0 1 1 1c0 1.25.2 2.45.57 3.57a1 1 0 0 1-.25 1z"/></svg>
      </p>
      <p class="contact-line">tobias@kelvaro.se
        <svg viewBox="0 0 24 24" aria-hidden="true"><rect x="3" y="5" width="18" height="14" rx="2" fill="none" stroke="#fff" stroke-width="2"/><path d="M3 7l9 6 9-6" fill="none" stroke="#fff" stroke-width="2"/></svg>
      </p>
    </div>
  </section>
</main>
</body>
</html>
```